依頼詳細
新しく設立した会社の名刺デザインの依頼です。
カチっとした硬い感じよりもロゴにあった感じのデザインでお願いします。
よろしくお願いいたします。
記載項目

・株式会社Lumo Taco
・代表取締役
・氏名
・名前ローマ字
・住所
・Tel
・Mobile
・mail

※レイアウトはお任せします※

・事業内容

プロフィール
・生年月日
・血液型
・星座
・出身地
・趣味
・資格

※レイアウトはお任せします※

氏名や住所などの記載事項はデザイン決定後にお知らせしますので、仮で入力をお願いします。
希望イメージ
シンプル 複雑
単色 カラフル
暗い 明るい
日常 高級
遊び心 厳粛
未来的 伝統的
女性的 男性的
希望する色
青系、水色系
納品ファイル
• 高解像度JPG (.jpg)
• イラストレーター形式 (.ai)
• フォトショップ形式 (.psd)
• PNG形式 (.png)
補足説明
ロゴを添付するのを忘れていました。申し訳御座いません。

表面のロゴがすごく目立っていて、
裏面にも遊び心があり気に入りました。

沢山のご提案ありがとうございました!
また、次の機会がありましたらどうぞよろしくお願い致します。

```html
<!DOCTYPE html>
<html lang="ja">
<head>
<meta charset="utf-8">
<title>Lumo Taco 名刺</title>
<link href="https://fonts.googleapis.com/css2?family=M+PLUS+Rounded+1c:wght@500;700&family=Noto+Sans+JP:wght@400;500;700&family=Noto+Serif+JP:wght@500&display=swap" rel="stylesheet">
<style>
  :root {
    --page: #e9eaeb;
    --card: #ffffff;
    --brand: #1aa3e0;
    --brand-light: #bfe3f6;
    --brand-pale: #dff1fb;
    --ink: #222;
    --ink-soft: #555;
  }
  * { margin: 0; padding: 0; box-sizing: border-box; }
  html, body { width: 865px; height: 1200px; overflow: hidden; background: var(--page); }
  body { position: relative; font-family: "Noto Sans JP", sans-serif; color: var(--ink); }

  .card {
    position: absolute; left: 81px; width: 703px; height: 433px;
    background: var(--card); box-shadow: 0 2px 6px rgba(0,0,0,.18); overflow: hidden;
  }
  .card--front { top: 63px; }
  .card--back { top: 657px; }

  .brand-mark { position: absolute; background: var(--brand); border-radius: 22px; z-index: 2; }
  .brand-name {
    position: absolute; font-family: "M PLUS Rounded 1c", sans-serif; font-weight: 700;
    color: var(--brand); white-space: nowrap; letter-spacing: 1px; z-index: 2;
  }

  /* front */
  .front-mark { left: 62px; top: 50px; width: 180px; height: 180px; border-radius: 30px; }
  .front-name { left: 38px; top: 258px; font-size: 54px; }

  .title { position: absolute; left: 420px; top: 62px; font-size: 14px; }
  .person-name {
    position: absolute; left: 392px; top: 96px;
    font-family: "Noto Serif JP", serif; font-size: 48px; letter-spacing: 10px; font-weight: 500;
  }
  .person-roman { position: absolute; left: 420px; top: 170px; font-size: 13px; color: var(--ink-soft); word-spacing: 40px; }
  .divider { position: absolute; left: 392px; top: 198px; width: 270px; height: 1px; background: #ccc; }
  .company { position: absolute; left: 392px; top: 214px; font-size: 19px; font-weight: 700; color: var(--ink-soft); }
  .contact { position: absolute; left: 392px; top: 250px; font-size: 12.5px; line-height: 22px; color: var(--ink-soft); }

  /* back */
  .back-mark { left: 40px; top: 44px; width: 60px; height: 60px; border-radius: 14px; }
  .back-name { left: 116px; top: 46px; font-size: 44px; }
  .back-deco {
    position: absolute; left: 410px; top: 70px; width: 260px; height: 330px;
    background: var(--brand-light); border-radius: 40px; opacity: .7; z-index: 1;
  }
  .services { position: absolute; left: 40px; top: 220px; }
  .services h2 { font-size: 16px; font-weight: 700; color: var(--brand); margin-bottom: 6px; }
  .services h2::before { content: ""; display: inline-block; width: 12px; height: 12px; background: var(--brand); margin-right: 4px; }
  .services li { list-style: none; font-family: "Noto Serif JP", serif; font-size: 16px; line-height: 27px; }
  .services li::before { content: "・"; }

  .profile { position: absolute; left: 428px; top: 230px; z-index: 2; }
  .profile-name {
    font-family: "Noto Serif JP", serif; font-size: 20px; letter-spacing: 4px;
    border-left: 6px solid var(--brand); padding-left: 8px; margin-bottom: 6px;
  }
  .profile li { list-style: none; font-size: 13px; line-height: 22px; }
  .profile li::before { content: "●"; color: var(--ink); margin-right: 2px; }
</style>
</head>
<body>

<section class="card card--front">
  <div class="brand-mark front-mark"></div>
  <div class="brand-name front-name">Lumo Taco</div>

  <div class="title">代表取締役</div>
  <div class="person-name">青木 健太</div>
  <div class="person-roman">Kenta Aoki</div>
  <div class="divider"></div>
  <div class="company">株式会社Lumo Taco</div>
  <div class="contact">
    〒812-0000 福岡県青葉市□□□□□<br>
    TEL:092-000-0000 FAX:092-000-0000<br>
    Mobile:080-0000-0000<br>
    Email:aoki@lumotaco.jp
  </div>
</section>

<section class="card card--back">
  <div class="brand-mark back-mark"></div>
  <div class="brand-name back-name">Lumo Taco</div>

  <div class="back-deco"></div>

  <div class="services">
    <h2>事業内容</h2>
    <ul>
      <li>化粧品・健康食品</li>
      <li>雑貨等のOEM受託製造</li>
      <li>通販商材の卸販売</li>
      <li>ネットショップの運営</li>
      <li>Webサイト企画、制作</li>
    </ul>
  </div>

  <div class="profile">
    <div class="profile-name">青木 健太</div>
    <ul>
      <li>2015年 8月10日</li>
      <li>A型</li>
      <li>獅子座</li>
      <li>福岡県生</li>
      <li>スポーツ観戦・読書・マラソン</li>
      <li>□□□□1級取得</li>
    </ul>
  </div>
</section>

</body>
</html>
```